Teachers workshop flyer

I need a flyer to inform schools of a workshop for teachers that empowers the teacher to help traumatised and disadvantaged students to engage in successful learning.

I am a teacher and educator and my info for the flyer is attached.

Target Market(s)

Principals and vice-principals who have stressed staff and students and they want things to be better in the school!

Industry/Entity Type

Teacher

```html
<!DOCTYPE html>
<html lang="en">
<head>
<meta charset="utf-8">
<title>Brain-based Strategies for Student Success</title>
<link href="https://fonts.googleapis.com/css2?family=Roboto+Condensed:wght@700&family=Arimo:ital,wght@0,400;0,700;1,400&display=swap" rel="stylesheet">
<style>
  :root {
    --board-green: #2c5a4f;
    --shirt-blue: #8fa6bd;
    --desk-grey: #6b6a66;
    --panel: rgba(70, 74, 78, 0.72);
    --gold: #f0b323;
    --gold-deep: #d99a12;
    --white: #ffffff;
    --bulb-yellow: rgba(246, 205, 60, 0.35);
  }
  html, body { margin: 0; padding: 0; overflow: hidden; background: #ddd; }
  .flyer {
    position: relative;
    width: 858px;
    height: 1200px;
    overflow: hidden;
    font-family: "Arimo", Arial, sans-serif;
    color: var(--white);
  }
  .backdrop {
    position: absolute; inset: 0;
    background:
      radial-gradient(ellipse 300px 420px at 520px 330px, rgba(190,150,120,0.55), transparent 70%),
      radial-gradient(ellipse 360px 520px at 560px 760px, rgba(170,190,215,0.8), transparent 72%),
      linear-gradient(180deg, var(--board-green) 0%, #3b6a5e 30%, #6f8a8c 55%, var(--shirt-blue) 72%, var(--desk-grey) 100%);
  }
  .bulb-doodle {
    position: absolute; left: 640px; top: 40px; width: 150px; height: 170px;
    border-radius: 50%;
    background: radial-gradient(circle, var(--bulb-yellow), transparent 70%);
  }
  .title {
    position: absolute; left: 58px; top: 26px; margin: 0;
    font-family: "Roboto Condensed", "Arial Narrow", sans-serif;
    font-weight: 700; font-size: 76px; line-height: 82px;
    letter-spacing: -0.5px;
    text-shadow: 0 2px 6px rgba(0,0,0,0.25);
  }
  .panel {
    position: absolute; left: 40px; width: 776px;
    background: var(--panel);
    border-radius: 4px;
    box-sizing: border-box;
  }
  .intro { top: 362px; height: 324px; padding: 14px 22px 0 24px; }
  .intro p { margin: 0 0 14px; font-size: 16.5px; line-height: 20px; text-align: justify; }
  .intro .presenter { margin: 0; }
  .feedback { top: 706px; height: 136px; padding: 40px 22px 0 24px; }
  .moments { top: 860px; height: 176px; padding: 40px 22px 0 24px; }
  .tab {
    position: absolute; left: 0; top: 8px;
    padding: 3px 40px 3px 24px;
    font-weight: 700; font-size: 17px; line-height: 22px; color: var(--white);
    background: linear-gradient(90deg, var(--gold-deep), var(--gold) 70%, rgba(240,179,35,0));
  }
  .feedback blockquote { margin: 0; font-size: 17px; line-height: 21px; text-align: justify; }
  .moments ul { margin: 0; padding: 0; list-style: none; }
  .moments li { position: relative; padding-left: 22px; font-size: 17px; line-height: 23px; }
  .moments li::before {
    content: ""; position: absolute; left: 0; top: 7px;
    width: 9px; height: 9px; border-radius: 50%; background: var(--gold);
  }
  .cta {
    position: absolute; left: 40px; top: 1076px; width: 776px; height: 84px;
    box-sizing: border-box; padding: 18px 0 0 150px;
    background: linear-gradient(90deg, rgba(40,40,40,0) 0%, rgba(40,40,40,0.55) 20%, rgba(40,40,40,0.55) 80%, rgba(40,40,40,0) 100%);
    border-top: 3px solid transparent; border-bottom: 3px solid transparent;
    border-image: linear-gradient(90deg, transparent, var(--gold) 20%, var(--gold) 80%, transparent) 1;
    color: var(--gold); font-weight: 700; font-size: 17px; line-height: 22px;
  }
  .cta p { margin: 0; }
</style>
</head>
<body>
<div class="flyer">
  <div class="backdrop" role="img" aria-label="Photograph of a smiling teacher in a striped shirt holding a tablet in front of a green classroom chalkboard"></div>
  <div class="bulb-doodle" role="img" aria-label="Hand-drawn yellow light bulb doodle"></div>

  <h1 class="title">Brain-based<br>Strategies<br>for Student<br>Success</h1>

  <section class="panel intro">
    <p>Contemporary teaching is a highly complex role as increasing numbers of students attend school without the essential ‘self-skills’ to be truly ‘school-ready’ and successful. Instead these students often seek-out attention in ways that can disruptive in the classroom causing stress and frustration for teachers.</p>
    <p>Dan shows how and why the most effective strategies for these students are guided by a sound understanding of child-development and brain-development – especially where trauma has left lasting impacts. Teachers can learn how to build a student’s self-skills, without the teacher having to become a therapist!</p>
    <p class="presenter">About the Presenter:<br>Daniel Hartley is a Melbourne-based therapist and educator with over twenty years experience working with adults and young people in the area of trauma and recovery. Dan’s seminars are engaging and practical since teachers need effective strategies that will immediately translate into classroom practice. Dan has trained here and overseas in the most effective behavior change strategies.</p>
  </section>

  <section class="panel feedback">
    <div class="tab">Teacher Feedback:</div>
    <blockquote>“Dan was such an engaging and energetic presenter whom I enjoyed immensely. His presentation on the brain and take away strategies were so practical and meaningful. It was an invaluable session.”</blockquote>
  </section>

  <section class="panel moments">
    <div class="tab">“My Light-bulb moments:</div>
    <ul>
      <li>I need to CONNECT – not correct – far more often.</li>
      <li>Seeing negative self-talk for what it is.</li>
      <li>Using far more ‘diversions’ in the avoidance loop.”</li>
    </ul>
  </section>

  <div class="cta">
    <p>Call 0412 555 019 for more information or to book Dan to come<br>to your school: www.danielhartley.com.au/studentsuccess</p>
  </div>
</div>
</body>
</html>
```